'Private English tutoring'

I need a flyer design to advertise private English tutoring. I am offering lessons to ethnic minority groups in my local area in south Belfast. The biggest ethnic minorities groups are Chinese, Polish and Indian and African. I can teach at any level, from beginner English to advanced. The tutoring will be either one on one or small groups of four students. I can teach adults and children but my preference would be to teach adults.

The flyer would need to be easily understood by people who have English as a second language.

I am also offering proof reading and editing services to students at local universities and colleges.

Target Market(s)

Adults of ethnic minorities who may not speak or read much English

Industry/Entity Type

Tutoring

Font styles to use
Serif

Requirements
Must have
• It needs to communicate that I am an accredited TEFL (Teaching English as a Foreign language) tutor with 2 years experience and that I tutor Beginners - Advanced students. It would also need to say that I offer proof reading and editing services. It would also need to communicate the cost of lessons are £15, but there are group rates for groups of 2-4 students. It would need to include my contact details which are as follows: contact Mona Hargrove BTh at 07812609354 or email monahargroveenglish@quillpost.com
Nice to have
• In terms of design I would like it to be warm and inviting and something which would convey an atmosphere of learning for non English speakers. Other than that I don't have any preferences.
Should not have
• Nothing which is going to be offensive to ethnic minorities.
• No pictures of people

```html
<!DOCTYPE html>
<html lang="en">
<head>
<meta charset="utf-8">
<title>Let's Speak English – Private English Tutoring</title>
<link href="https://fonts.googleapis.com/css2?family=Oswald:wght@400;500;600;700&display=swap" rel="stylesheet">
<style>
  :root{
    --brown:#3b2a20;
    --brown-deep:#2a1d16;
    --blue:#2aa7df;
    --yellow:#f6e500;
    --white:#ffffff;
    --ink:#2b211b;
    --desk-light:#d9d4cc;
    --desk-mid:#9c958c;
    --desk-dark:#5f5750;
  }
  *{margin:0;padding:0;box-sizing:border-box}
  html,body{width:851px;height:1200px;overflow:hidden;background:var(--white)}
  .flyer{position:relative;width:851px;height:1200px;overflow:hidden;font-family:'Oswald',sans-serif;background:var(--brown)}

  .hero-photo{position:absolute;left:0;top:0;width:851px;height:420px;
    background:linear-gradient(160deg,var(--desk-light) 0%,#c4beb5 35%,var(--desk-mid) 70%,var(--desk-dark) 100%)}

  .bubble{position:absolute}
  .bubble-hi{left:28px;top:14px;width:190px;height:180px}
  .bubble-hello{left:567px;top:180px;width:205px;height:180px}

  .headline-band{position:absolute;left:0;top:420px;width:851px;height:247px;background:var(--white);text-align:center}
  .headline{margin-top:40px;font-size:84px;font-weight:600;letter-spacing:1px;color:var(--ink);line-height:1;text-transform:uppercase;white-space:nowrap}
  .headline .accent{color:var(--blue)}
  .subhead{margin-top:26px;font-size:27px;font-weight:500;color:var(--ink);letter-spacing:.4px;text-transform:uppercase;white-space:nowrap}

  .services{position:absolute;left:0;top:667px;width:851px;height:392px;background:var(--brown)}
  .world-map{position:absolute;left:560px;top:70px;width:270px;height:150px;
    background:radial-gradient(ellipse at center,rgba(246,229,0,.35) 0%,rgba(246,229,0,.12) 60%,rgba(246,229,0,0) 75%)}

  .service{position:absolute;left:0;height:52px;background:var(--blue);color:var(--white);
    font-size:19px;font-weight:500;letter-spacing:.5px;text-transform:uppercase;display:flex;align-items:center;padding-left:100px;white-space:nowrap}
  .service .icon{position:absolute;left:28px;top:10px;width:34px;height:32px;background:var(--white);display:flex;align-items:center;justify-content:center}
  .service-tefl{top:50px;width:642px}
  .service-proof{top:138px;width:642px}
  .service-courses{top:228px;width:805px}

  .rates{position:absolute;left:0;top:300px;width:851px;height:52px;background:var(--yellow);color:var(--brown-deep);
    font-size:19px;font-weight:500;letter-spacing:.3px;display:flex;align-items:center;padding-left:28px;text-transform:uppercase;white-space:nowrap}

  .footer{position:absolute;left:0;top:1059px;width:851px;height:141px;background:var(--brown-deep);display:flex;align-items:center}
  .credential{display:flex;align-items:center;margin-left:28px;color:var(--yellow)}
  .credential .tefl{font-size:50px;font-weight:600;line-height:1}
  .credential .divider{width:3px;height:54px;background:var(--yellow);margin:0 14px}
  .credential .label{font-size:20px;font-weight:500;line-height:1.2;text-transform:uppercase}
  .phone-badge{margin-left:80px;width:66px;height:66px}
  .contact{margin-left:20px;color:var(--white);font-size:19px;font-weight:500;line-height:1.45;text-transform:uppercase;letter-spacing:.3px;font-style:normal;white-space:nowrap}
</style>
</head>
<body>
<div class="flyer">

  <div class="hero-photo" role="img" aria-label="Soft-focus photo of a desk with a white coffee mug and a smartphone"></div>

  <svg class="bubble bubble-hi" viewBox="0 0 190 180" aria-label="Speech bubble saying Hi!">
    <path d="M95 8a82 76 0 1 1-52 142l-30 18 12-34A82 76 0 0 1 95 8z" fill="var(--blue)"/>
    <path d="M92 4a80 74 0 1 1-50 138l-30 18 12-34A80 74 0 0 1 92 4z" fill="var(--yellow)"/>
    <text x="92" y="100" text-anchor="middle" font-family="Oswald,sans-serif" font-size="58" font-weight="600" fill="#2a1d16">HI!</text>
  </svg>

  <svg class="bubble bubble-hello" viewBox="0 0 205 180" aria-label="Speech bubble saying Hello!">
    <path d="M110 10a86 72 0 1 0 52 136l32 22-12-36A86 72 0 0 0 110 10z" fill="var(--yellow)"/>
    <path d="M106 6a86 72 0 1 0 52 136l32 22-12-36A86 72 0 0 0 106 6z" fill="var(--blue)"/>
    <text x="104" y="94" text-anchor="middle" font-family="Oswald,sans-serif" font-size="42" font-weight="600" fill="#ffffff">HELLO!</text>
  </svg>

  <section class="headline-band">
    <h1 class="headline">Let's <span class="accent">Speak</span> English!</h1>
    <p class="subhead">Private English tutoring for beginner to advanced students</p>
  </section>

  <section class="services">
    <div class="world-map" role="img" aria-label="Yellow dotted world map decoration"></div>

    <div class="service service-tefl">
      <span class="icon"><svg width="20" height="20" viewBox="0 0 20 20"><circle cx="10" cy="6" r="4" fill="var(--blue)"/><path d="M2 19a8 7 0 0 1 16 0z" fill="var(--blue)"/></svg></span>
      Accredited TEFL tutor with 2 years experience
    </div>
    <div class="service service-proof">
      <span class="icon"><svg width="18" height="20" viewBox="0 0 18 20"><path d="M2 1h10l4 4v14H2z" fill="var(--blue)"/><path d="M5 9h8M5 12h8M5 15h6" stroke="#fff" stroke-width="1.5"/></svg></span>
      Proof reading and editing services
    </div>
    <div class="service service-courses">
      <span class="icon"><svg width="22" height="20" viewBox="0 0 22 20"><ellipse cx="11" cy="9" rx="10" ry="7.5" fill="var(--blue)"/><path d="M5 14l-2 5 6-3z" fill="var(--blue)"/></svg></span>
      One-to-one courses &amp; personalised group courses for up to 4 people
    </div>

    <div class="rates">£15 per hour - group rates for groups of 2 - 4 students - contact me for more details</div>
  </section>

  <footer class="footer">
    <div class="credential">
      <span class="tefl">TEFL</span>
      <span class="divider"></span>
      <span class="label">Accredited<br>Tutor</span>
    </div>
    <svg class="phone-badge" viewBox="0 0 66 66" aria-label="Phone">
      <circle cx="33" cy="33" r="31" fill="var(--blue)"/>
      <path d="M22 18c2-2 4-2 5 0l3 6c1 2 0 3-1 4l-2 2c2 5 6 9 11 11l2-2c1-1 2-2 4-1l6 3c2 1 2 3 0 5l-3 3c-3 3-12 0-19-7s-10-16-7-19z" fill="#fff"/>
    </svg>
    <address class="contact">
      Contact Mona Hargrove BTh at 07812609354<br>
      or email monahargroveenglish@quillpost.com
    </address>
  </footer>

</div>
</body>
</html>
```